Dröm website

I need a website that I can talk about the company, mission statement and my background on a page. I need a section where customers can order eqipment , pay for it and be able to search for equipment by brand name or model number, schedule an appointment with the tech and a page for general information such as any promotions I'm having, tips on getting good sleep and developing technology news or updates in sleep medicine. I would like a quick link to facebook and twitter. I will also need a way to upload instructional videos.
Updates

Please check out www.RestaloGear.com for ideas. This is a company like the one I have except I am not all online like they are. I see clients face to face also. I also chose coded but the brief did not save that choice. The website should be coded. Added Monday, June 20, 2016

Target Market(s)

Clients with sleep disorders, need a home sleep study done, who have been denied by insurance or have a large insurance deductible and clients who need an option for a payment plan. Clients age 35-70. Physicians offices and other medical professionals.

Coding

Coded - Design and coding required

Number of Pages Required

5+ page

Font styles to use
Other font styles liked:
• Leave it up to the designer

Requirements
Must have
• User friendly, easy to read lettering, able to put pictures on the website, able to update often, secure payment for supplies, credit card only, able to upload videos, my contact information, "contact me" link, my logo and business name.
Nice to have
• A changing information banner on 1st page to highlight and link to any specials promotions or sales or news.
Should not have
• No cartoon animation,

```html
<!DOCTYPE html>
<html lang="en">
<head>
<meta charset="utf-8">
<title>Dröm – Sleep Care Equipment</title>
<link href="https://fonts.googleapis.com/css2?family=Raleway:wght@400;600;700;800&family=Open+Sans:wght@400;600;700&display=swap" rel="stylesheet">
<style>
:root{
  --blue:#3f9fcf;
  --blue-dark:#3890bd;
  --blue-deep:#2f7fac;
  --orange:#f7a21b;
  --ink:#3d3d3d;
  --muted:#8a8a8a;
  --white:#ffffff;
  --night:#16181c;
  --line:#e3e3e3;
}
*{margin:0;padding:0;box-sizing:border-box}
html,body{width:1200px;height:3020px;overflow:hidden;background:var(--white)}
body{font-family:"Open Sans",Arial,sans-serif;color:var(--ink)}
.page{position:relative;width:1200px;height:3020px;overflow:hidden}
.abs{position:absolute}
h1,h2,h3,h4,.nav a,.btn{font-family:"Raleway",Arial,sans-serif}

/* header */
.site-header{position:absolute;left:0;top:0;width:1200px;height:108px;background:var(--white)}
.brand{position:absolute;left:100px;top:26px;display:flex;align-items:center;gap:12px}
.brand-mark{width:44px;height:44px;border-radius:50%;background:var(--blue)}
.brand-name{font-family:"Raleway",Arial,sans-serif;font-weight:600;font-size:40px;color:var(--blue)}
.call{position:absolute;left:744px;top:24px;font-size:12px;color:var(--muted);display:flex;align-items:center;gap:6px}
.call b{color:var(--orange);font-weight:600}
.search-icon{position:absolute;left:946px;top:26px}
.btn{display:inline-flex;align-items:center;justify-content:center;background:var(--orange);color:var(--white);font-weight:700;font-size:12px;letter-spacing:.4px;text-transform:uppercase}
.book{position:absolute;left:982px;top:16px;width:118px;height:34px}
.nav{position:absolute;top:74px;left:0;width:1200px;height:34px}
.nav a{position:absolute;top:0;font-size:11.5px;font-weight:700;color:#444;text-decoration:none;text-transform:uppercase;height:34px}
.nav a.active{border-bottom:2px solid var(--blue)}

/* hero */
.hero{position:absolute;left:0;top:108px;width:1200px;height:470px}
.hero-photo{position:absolute;inset:0;background:linear-gradient(100deg,#2a2e3a 0%,#6b7088 30%,#b9bdd0 55%,#d7d8e4 75%,#8d90a3 100%)}
.hero h1{position:absolute;left:96px;top:326px;font-size:40px;font-weight:700;color:var(--white);letter-spacing:.5px}
.hero p{position:absolute;left:96px;top:380px;font-family:"Raleway",Arial,sans-serif;font-size:20px;font-weight:700;color:#1d1d1d;text-transform:uppercase}
.dots{position:absolute;left:578px;top:442px;display:flex;gap:6px}
.dots i{width:7px;height:7px;border-radius:50%;background:rgba(255,255,255,.6)}
.dots i:first-child{background:var(--blue)}

/* order */
.order{position:absolute;left:0;top:578px;width:1200px;height:320px}
.order-wave{position:absolute;left:0;top:0}
.order h2{position:absolute;top:66px;width:1200px;text-align:center;font-size:29px;font-weight:700;color:var(--white);text-transform:uppercase}
.order .lead{position:absolute;top:114px;width:1200px;text-align:center;font-size:12px;color:var(--white)}
.order label{position:absolute;left:164px;top:180px;font-size:13px;color:var(--white)}
.order .field{position:absolute;left:312px;top:168px;width:534px;height:44px;background:var(--white);font-size:12.5px;color:#999;padding:14px 18px}
.order .go{position:absolute;left:860px;top:168px;width:166px;height:44px;gap:8px}
.chev{position:absolute;left:582px;top:272px}

/* features */
.feature{position:absolute;width:330px}
.feature .ico{position:absolute;left:0;top:0;width:54px;height:54px;border-radius:50%;background:var(--blue);display:flex;align-items:center;justify-content:center}
.feature h3{position:absolute;left:100px;top:14px;font-size:13px;font-weight:700;color:#444;text-transform:uppercase}
.feature p{position:absolute;left:100px;top:38px;width:230px;font-size:12.5px;line-height:22px;color:var(--muted)}
.promo{position:absolute;left:842px;top:964px;width:258px;height:258px;overflow:hidden}
.promo-photo{position:absolute;inset:0;background:linear-gradient(180deg,#6aa6d8 0%,#a8cdea 55%,#5aa23a 80%,#3f8a2a 100%)}
.promo h4{position:absolute;left:24px;top:192px;font-size:16px;font-weight:800;color:var(--white);text-transform:uppercase}
.promo span{position:absolute;left:24px;top:220px;font-family:"Raleway",Arial,sans-serif;font-size:15px;color:#f2e34a}
.promo .btn{position:absolute;left:152px;top:214px;width:84px;height:28px;font-size:10px}

/* appointment band */
.band{position:absolute;left:0;top:1306px;width:1200px;height:344px}
.band-photo{position:absolute;inset:0;background:radial-gradient(ellipse at 72% 50%,#4a4a4e 0%,#24252a 35%,var(--night) 70%)}
.band p{position:absolute;left:190px;top:104px;width:820px;text-align:center;font-size:17px;line-height:32px;color:var(--white)}
.band .btn{position:absolute;left:478px;top:192px;width:244px;height:50px}

/* how it works */
.section-title{position:absolute;width:1200px;text-align:center;font-size:30px;font-weight:700;color:#444;text-transform:uppercase;letter-spacing:.5px}
.how-lead{position:absolute;left:190px;top:1774px;width:820px;text-align:center;font-size:17px;line-height:32px;font-weight:600;color:#666}
.video{position:absolute;left:258px;top:1872px;width:682px;height:398px;overflow:hidden}
.video-still{position:absolute;inset:0;background:linear-gradient(135deg,#3b2a20 0%,#5a4334 30%,#c9ccd6 55%,#2c3a66 80%,#1a2245 100%)}
.play{position:absolute;left:295px;top:152px}
.controls{position:absolute;left:0;bottom:0;width:682px;height:30px;background:rgba(0,0,0,.75)}
.controls .bar{position:absolute;left:52px;top:13px;width:500px;height:4px;background:#555}
.controls .host{position:absolute;left:620px;top:9px;width:48px;height:12px;background:#888}

/* testimonials */
.quote{position:absolute;width:300px}
.quote .q{position:absolute;font-family:Georgia,serif;font-size:34px;color:#bbb;line-height:1}
.quote p{position:absolute;left:30px;top:0;width:240px;font-size:12.5px;line-height:23px;color:#666}
.quote .avatar{position:absolute;left:0;top:106px;width:56px;height:56px;border-radius:50%;background:linear-gradient(180deg,#c9b6a4,#8a6e5c);border:2px solid #ddd}
.quote .who{position:absolute;left:76px;top:120px;font-family:"Raleway",Arial,sans-serif;font-size:12px;font-weight:700;color:var(--blue);text-transform:uppercase}
.quote .role{position:absolute;left:76px;top:140px;font-size:12px;color:var(--muted)}

/* footer */
.footer{position:absolute;left:0;top:2674px;width:1200px;height:286px;background:var(--blue)}
.footer h4{position:absolute;top:52px;font-size:14px;font-weight:700;color:var(--white);text-transform:uppercase}
.footer ul{position:absolute;top:90px;list-style:none}
.footer li{font-size:12px;line-height:24px;color:var(--white)}
.post{position:absolute;left:104px;width:272px;color:var(--white);border-bottom:1px solid rgba(255,255,255,.25);padding-bottom:10px}
.post:last-of-type{border-bottom:none}
.post-title,.post-date{display:block;font-size:10.5px;font-weight:600;line-height:22px;white-space:nowrap}
.arrows{position:absolute;left:354px;top:50px;color:var(--white);font-size:14px;letter-spacing:6px}
.social{position:absolute;left:876px;top:90px;font-size:11px;color:var(--white)}
.social-row{position:absolute;left:876px;top:124px;display:flex;gap:10px}
.social-row i{width:28px;height:28px;border-radius:50%;background:var(--white)}
.foot-brand{position:absolute;left:876px;top:176px;display:flex;align-items:center;gap:12px}
.foot-brand .dot{width:40px;height:40px;border-radius:50%;background:var(--white)}
.foot-brand span{font-family:"Raleway",Arial,sans-serif;font-weight:600;font-size:38px;color:var(--white)}
.bottom{position:absolute;left:0;top:2960px;width:1200px;height:60px;background:var(--blue-deep);color:var(--white);font-size:12px;text-align:center;line-height:60px}
</style>
</head>
<body>
<div class="page">

  <header class="site-header">
    <div class="brand"><div class="brand-mark"></div><span class="brand-name">Dröm</span></div>
    <div class="call">
      <svg width="12" height="12" viewBox="0 0 24 24"><path fill="#f7a21b" d="M6.6 10.8a15 15 0 006.6 6.6l2.2-2.2c.3-.3.7-.4 1-.2 1.1.4 2.3.6 3.6.6.6 0 1 .4 1 1V20c0 .6-.4 1-1 1A17 17 0 013 4c0-.6.4-1 1-1h3.5c.6 0 1 .4 1 1 0 1.3.2 2.5.6 3.6.1.3 0 .7-.2 1z"/></svg>
      Call Us : <b>(6523) 481 207</b>
    </div>
    <svg class="search-icon" width="14" height="14" viewBox="0 0 24 24"><circle cx="10" cy="10" r="7" fill="none" stroke="#999" stroke-width="2.5"/><path d="M15 15l6 6" stroke="#999" stroke-width="2.5"/></svg>
    <a class="btn book">Book Now</a>
    <nav class="nav">
      <a class="active" style="left:500px">Home</a>
      <a style="left:604px">About Us</a>
      <a style="left:736px">Services</a>
      <a style="left:860px">How It Works</a>
      <a style="left:1022px">Contact Us</a>
    </nav>
  </header>

  <section class="hero">
    <div class="hero-photo" role="img" aria-label="Photo of a tired woman lying awake in bed on white pillows"></div>
    <h1>WE SPECIALISE IN</h1>
    <p>Automotive collision, brake, and tire services</p>
    <div class="dots"><i></i><i></i><i></i><i></i></div>
  </section>

  <section class="order">
    <svg class="order-wave" width="1200" height="320" viewBox="0 0 1200 320">
      <path d="M0 0H1200V278C1000 278 760 276 680 268C620 262 600 300 560 300C520 300 520 270 470 272C380 276 200 278 0 278Z" fill="#3f9fcf"/>
    </svg>
    <h2>Customers can order equipment</h2>
    <p class="lead">Lorem Ipsum is simply dummy text of the printing and typesetting industry. Lorem Ipsum has been the industry's standard dummy...</p>
    <label>Search for equipment</label>
    <div class="field">Brand name or model number</div>
    <a class="btn go">
      <svg width="12" height="12" viewBox="0 0 24 24"><circle cx="10" cy="10" r="7" fill="none" stroke="#fff" stroke-width="3"/><path d="M15 15l6 6" stroke="#fff" stroke-width="3"/></svg>
      Search Now
    </a>
    <svg class="chev" width="36" height="20" viewBox="0 0 36 20"><path d="M4 3l14 7 14-7M4 10l14 7 14-7" fill="none" stroke="#fff" stroke-width="2"/></svg>
  </section>

  <section class="features">
    <div class="feature abs" style="left:98px;top:966px">
      <div class="ico"><svg width="28" height="28" viewBox="0 0 28 28" fill="none" stroke="#fff" stroke-width="2"><circle cx="14" cy="8" r="5"/><path d="M12.5 7a1.5 1.5 0 113 0c0 1-1.5 1.2-1.5 2.5"/><path d="M3 14v10M3 20h22v4M3 17h22"/></svg></div>
      <h3>Sleep Disorders</h3>
      <p>Lorem Ipsum is simply dummy text of the printing and typesetting industry. Lorem Ipsum has been the industry...</p>
    </div>
    <div class="feature abs" style="left:474px;top:966px">
      <div class="ico"><svg width="28" height="28" viewBox="0 0 28 28" fill="none" stroke="#fff" stroke-width="2"><path d="M3 8v14M3 18h22v4M11 13h12a2 2 0 012 2v3"/><circle cx="7" cy="14" r="2"/></svg></div>
      <h3>Sleep Study Done</h3>
      <p>Lorem Ipsum is simply dummy text of the printing and typesetting industry. Lorem Ipsum has been the industry...</p>
    </div>
    <div class="feature abs" style="left:98px;top:1120px">
      <div class="ico"><svg width="28" height="28" viewBox="0 0 28 28" fill="none" stroke="#fff" stroke-width="2"><path d="M3 14a11 9 0 0122 0zM14 14v9a2 2 0 01-4 0"/></svg></div>
      <h3>Denied by Insurance</h3>
      <p>Lorem Ipsum is simply dummy text of the printing and typesetting industry. Lorem Ipsum has been the industry...</p>
    </div>
    <div class="feature abs" style="left:474px;top:1120px">
      <div class="ico"><svg width="28" height="28" viewBox="0 0 28 28"><path d="M14 3l9 3v7c0 6-4 10-9 12-5-2-9-6-9-12V6z" fill="#fff"/><path d="M10 14l3 3 5-6" fill="none" stroke="#3f9fcf" stroke-width="2.2"/></svg></div>
      <h3>Insurance Deductible</h3>
      <p>Lorem Ipsum is simply dummy text of the printing and typesetting industry. Lorem Ipsum has been the industry...</p>
    </div>
    <div class="promo">
      <div class="promo-photo" role="img" aria-label="Photo of two happy people jumping on a green hill under a blue sky"></div>
      <h4>How to be happy</h4>
      <span>...and less tired</span>
      <a class="btn">Click Here</a>
    </div>
  </section>

  <section class="band">
    <div class="band-photo" role="img" aria-label="Dark photo of a sleepless woman resting her head on her hand"></div>
    <p>Lorem Ipsum is simply dummy text of the printing and typesetting industry. Lorem Ipsum has been the industry's standard dummy text ever since the 1500s</p>
    <a class="btn">Schedule an Appointment</a>
  </section>

  <section class="how">
    <h2 class="section-title" style="top:1720px">How it works</h2>
    <p class="how-lead">Lorem Ipsum is simply dummy text of the printing and typesetting industry. Lorem Ipsum has been the industry's standard dummy text ever since the 1500s</p>
    <div class="video">
      <div class="video-still" role="img" aria-label="Video still of an older couple asleep in bed with a sleep therapy machine on the nightstand"></div>
      <svg class="play" width="92" height="92" viewBox="0 0 92 92"><circle cx="46" cy="46" r="42" fill="none" stroke="#fff" stroke-width="5"/><path d="M37 28l28 18-28 18z" fill="#fff"/></svg>
      <div class="controls">
        <svg class="abs" style="left:18px;top:9px" width="12" height="12" viewBox="0 0 12 12"><path d="M2 1l9 5-9 5z" fill="#fff"/></svg>
        <div class="bar"></div>
        <div class="host"></div>
      </div>
    </div>
  </section>

  <section class="clients">
    <h2 class="section-title" style="top:2350px">What our clients say</h2>
    <div class="quote" style="left:100px;top:2430px">
      <span class="q" style="left:0;top:-6px">“</span><span class="q" style="left:272px;top:68px">”</span>
      <p>Lorem Ipsum is simply dummy text of the printing and typesetting industry. Lorem Ipsum has been the industry's standard dummy text ever since...</p>
      <div class="avatar" role="img" aria-label="Client portrait"></div>
      <div class="who">Marlon Keats</div><div class="role">Business man</div>
    </div>
    <div class="quote" style="left:456px;top:2430px">
      <span class="q" style="left:0;top:-6px">“</span><span class="q" style="left:272px;top:68px">”</span>
      <p>Lorem Ipsum is simply dummy text of the printing and typesetting industry. Lorem Ipsum has been the industry's standard dummy text ever since...</p>
      <div class="avatar" role="img" aria-label="Client portrait"></div>
      <div class="who">Marlon Keats</div><div class="role">Business man</div>
    </div>
    <div class="quote" style="left:810px;top:2430px">
      <span class="q" style="left:0;top:-6px">“</span><span class="q" style="left:272px;top:68px">”</span>
      <p>Lorem Ipsum is simply dummy text of the printing and typesetting industry. Lorem Ipsum has been the industry's standard dummy text ever since...</p>
      <div class="avatar" role="img" aria-label="Client portrait"></div>
      <div class="who">Marlon Keats</div><div class="role">Business man</div>
    </div>
  </section>

  <footer class="footer">
    <h4 style="left:104px">Latest Posts</h4>
    <div class="arrows">‹ ›</div>
    <div class="post" style="top:84px"><span class="post-title">Lorem Ipsum is simply dummy text of the printing</span><span class="post-date">Posted on 27 March 2016</span></div>
    <div class="post" style="top:150px"><span class="post-title">Lorem Ipsum is simply dummy text of the printing</span><span class="post-date">Posted on 27 March 2016</span></div>
    <div class="post" style="top:216px"><span class="post-title">Lorem Ipsum is simply dummy text of the printing</span><span class="post-date">Posted on 27 March 2016</span></div>

    <h4 style="left:488px">Welcome</h4>
    <ul style="left:488px"><li>Home</li><li>About us</li><li>Services</li><li>How it works</li><li>Testimonials</li><li>Contact us</li></ul>

    <h4 style="left:680px">Information</h4>
    <ul style="left:680px"><li>Terms &amp; Conditions</li><li>Privacy Policy</li><li>Disclaimer</li><li>Sitemap</li></ul>

    <h4 style="left:876px">Follow Us</h4>
    <div class="social">Connect with our social media network</div>
    <div class="social-row"><i></i><i></i><i></i><i></i><i></i></div>
    <div class="foot-brand"><div class="dot"></div><span>Dröm</span></div>
  </footer>
  <div class="bottom">© 2016. Dröm. All rights reserved.</div>

</div>
</body>
</html>
```